Looking for a cool & simple business-card-design for digital agency

Hi!

We are a web agency that offers Reputation Management, Zorvik & Seo Services and software development. We like cool things, we like innovative styles.

We have uploaded our logo.

Project Deadline Extended Reason: Client does not want any designs with the colorful logo. Please send us submissions ONLY with the blac and white logo. What the client would like to see:1) Back of the card: is a silver logo on a black background2) front of the card with all the data, please use white background and black logo thank you Added Friday, May 8, 2015

Software

```html
<!DOCTYPE html>
<html lang="de">
<head>
<meta charset="utf-8">
<title>Nordvale AG – Geschäftsausstattung</title>
<link rel="stylesheet" href="https://fonts.googleapis.com/css2?family=Saira:wght@700&family=Lato:wght@400;700&display=swap">
<style>
  :root {
    --ink: #0c0c0c;
    --paper: #ffffff;
    --backdrop: #e7e7e7;
    --body-text: #555555;
    --muted: #8a8a8a;
    --pill: #b9b9b9;
    --silver: #d9d9d9;
  }
  * { box-sizing: border-box; margin: 0; padding: 0; }
  html, body { width: 1200px; height: 1200px; overflow: hidden; }
  body {
    background: var(--backdrop);
    font-family: "Lato", Arial, sans-serif;
    position: relative;
    color: var(--ink);
  }
  .piece { position: absolute; box-shadow: 0 2px 6px rgba(0,0,0,.18); }

  /* brand lockup */
  .brand { display: flex; align-items: center; gap: 10px; }
  .brand-square { width: 18px; height: 18px; background: currentColor; flex: none; }
  .brand-name { font-family: "Saira", Arial, sans-serif; font-weight: 700; font-size: 24px; line-height: 1; white-space: nowrap; }

  /* folder */
  .folder { left: 243px; top: 103px; width: 425px; height: 600px; background: var(--ink); color: var(--paper);
    display: flex; align-items: center; justify-content: center; }
  .folder .brand-name { font-size: 36px; }
  .folder .brand-square { width: 26px; height: 26px; }

  /* letterhead */
  .letterhead { left: 691px; top: 103px; width: 427px; height: 600px; background: var(--paper); }
  .letterhead-header { position: absolute; left: 0; right: 0; top: 18px; display: flex; justify-content: center; }
  .letterhead-header .brand-name { font-size: 17px; }
  .letterhead-header .brand-square { width: 12px; height: 12px; }
  .letterhead-rule { position: absolute; left: 0; right: 0; top: 53px; height: 1px; background: #cfcfcf; }
  .letter-body { position: absolute; left: 47px; right: 18px; top: 172px; font-size: 6.3px; line-height: 1.35; color: var(--body-text); text-align: justify; }
  .letter-body p { margin-bottom: 7px; }
  .letterhead-footer { position: absolute; left: 0; right: 0; bottom: 0; height: 45px; background: var(--ink); color: var(--paper);
    display: flex; align-items: center; font-size: 6.5px; }
  .footer-signer { width: 130px; padding-left: 47px; line-height: 1.3; }
  .footer-signer strong { font-size: 7px; }
  .footer-contacts, .footer-address { border-left: 1px solid #777; padding-left: 12px; margin-left: 0; line-height: 1.45; }
  .footer-contacts { width: 140px; margin-left: 4px; }
  .footer-address { padding-left: 22px; }
  .ico { display: inline-block; width: 6px; height: 6px; background: var(--paper); border-radius: 50%; margin-right: 4px; vertical-align: middle; }

  /* business card front */
  .card-front { left: 102px; top: 743px; width: 336px; height: 200px; background: var(--paper); }
  .card-front .brand { position: absolute; left: 0; right: 0; top: 34px; justify-content: center; }
  .card-name { position: absolute; left: 84px; top: 100px; width: 168px; height: 28px; border-radius: 14px; background: var(--pill);
    display: flex; align-items: center; justify-content: center; gap: 9px; font-size: 11px; }
  .card-name strong { font-weight: 700; }
  .card-name .divider { width: 1px; height: 16px; background: var(--ink); }
  .card-name .role { font-size: 9px; }
  .card-contacts { position: absolute; left: 0; right: 0; top: 147px; display: flex; justify-content: center; gap: 8px; font-size: 9.5px; }
  .card-contacts svg { width: 9px; height: 9px; vertical-align: -1px; margin-right: 2px; }
  .card-band { position: absolute; left: 0; right: 0; bottom: 0; height: 22px; background: var(--ink); }

  /* business card back */
  .card-back { left: 102px; top: 970px; width: 336px; height: 201px; background: var(--ink); color: var(--silver); }
  .card-back .brand { position: absolute; left: 18px; top: 68px; }
  .card-back .brand-name { font-size: 30px; }
  .card-back .brand-square { width: 32px; height: 32px; }
  .card-back-services { position: absolute; left: 110px; right: 14px; top: 123px; text-align: center; font-size: 9.5px; line-height: 1.4; color: var(--silver); }

  /* envelope */
  .envelope { left: 580px; top: 743px; width: 537px; height: 373px; background: var(--paper); }
  .envelope-flap { position: absolute; left: 0; top: 0; width: 100%; height: 103px; background: var(--ink);
    border-radius: 60px 60px 0 0 / 40px 40px 0 0; }
  .envelope .brand { position: absolute; left: 32px; top: 151px; }
  .envelope .brand-name { font-size: 19px; }
  .envelope .brand-square { width: 14px; height: 14px; }
  .envelope-address { position: absolute; right: 25px; top: 140px; text-align: right; font-size: 8px; line-height: 1.35; }
  .envelope-footer { position: absolute; left: 0; right: 0; bottom: 0; height: 24px; background: var(--ink); color: var(--paper);
    display: flex; align-items: center; gap: 38px; padding-left: 40px; font-size: 7.5px; }
</style>
</head>
<body>

<section class="piece folder">
  <div class="brand"><span class="brand-square"></span><span class="brand-name">Nordvale AG</span></div>
</section>

<section class="piece letterhead">
  <header class="letterhead-header">
    <div class="brand"><span class="brand-square"></span><span class="brand-name">Nordvale AG</span></div>
  </header>
  <div class="letterhead-rule"></div>
  <div class="letter-body">
    <p>Dear Alex Reed,</p>
    <p>Lorem ipsum dolor sit amet, consectetuer adipiscing elit, sed diam nonummy nibh euismod tincidunt ut laoreet dolore magna aliquam erat volutpat. Ut wisi enim ad minim veniam, quis nostrud exerci tation ullamcorper suscipit lobortis nisl ut aliquip ex ea commodo consequat. Duis autem vel eum iriure dolor in hendrerit in vulputate velit esse molestie consequat.</p>
    <p>Investigationes demonstraverunt lectores legere me lius quod ii legunt saepius. Claritas est etiam processus dynamicus, qui sequitur mutationem consuetudium lectorum.</p>
    <p>Lorem ipsum dolor sit amet, consectetuer adipiscing elit, sed diam nonummy nibh euismod tincidunt ut laoreet dolore magna aliquam erat volutpat. Ut wisi enim ad minim veniam, quis nostrud exerci tation ullamcorper suscipit lobortis nisl ut aliquip ex ea commodo consequat. Duis autem vel eum iriure dolor in hendrerit in vulputate velit esse molestie consequat.</p>
    <p>Yours Sincerely</p>
  </div>
  <footer class="letterhead-footer">
    <div class="footer-signer"><strong>Maren Holt</strong><br>Director</div>
    <div class="footer-contacts">
      <div><span class="ico"></span>000 555 0142</div>
      <div><span class="ico"></span>info@nordvaleag.com</div>
      <div><span class="ico"></span>www.nordvaleag.com</div>
    </div>
    <div class="footer-address">Address Line One , Suit #1111<br>Address line Two</div>
  </footer>
</section>

<section class="piece card-front">
  <div class="brand"><span class="brand-square"></span><span class="brand-name">Nordvale AG</span></div>
  <div class="card-name"><strong>Maren Holt</strong><span class="divider"></span><span class="role">Director</span></div>
  <div class="card-contacts">
    <span><svg viewBox="0 0 10 10"><path d="M2 1h2l1 2.5-1.3 1a5 5 0 0 0 2.8 2.8l1-1.3L10 7v2a1 1 0 0 1-1 1A9 9 0 0 1 0 2a1 1 0 0 1 1-1z" fill="currentColor"/></svg>000 555 0142</span>
    <span><svg viewBox="0 0 10 10"><rect x="0" y="1.5" width="10" height="7" fill="currentColor"/><path d="M0 1.5l5 4 5-4" stroke="#fff" fill="none"/></svg>info@nordvaleag.com</span>
    <span><svg viewBox="0 0 10 10"><circle cx="5" cy="5" r="5" fill="currentColor"/><path d="M0 5h10M5 0v10" stroke="#fff" stroke-width=".8"/></svg>www.nordvaleag.com</span>
  </div>
  <div class="card-band"></div>
</section>

<section class="piece card-back">
  <div class="brand"><span class="brand-square"></span><span class="brand-name">Nordvale AG</span></div>
  <p class="card-back-services">Reputation Management, Zorvik &amp; Seo Services<br>and Software development.</p>
</section>

<section class="piece envelope">
  <div class="envelope-flap"></div>
  <div class="brand"><span class="brand-square"></span><span class="brand-name">Nordvale AG</span></div>
  <div class="envelope-address">Address Line One , Suit #1111<br>Address line Two</div>
  <footer class="envelope-footer">
    <span>000 555 0142</span>
    <span>info@nordvaleag.com</span>
    <span>www.nordvaleag.com</span>
  </footer>
</section>

</body>
</html>
```